Aerospace Center needs app design

We need a design that would be a creative and innovative look of a simple idea connecting air traffic control situations with sonification.
We would like to see designs that use the elements shown in the short video which are different pads, showing 4 different colors, connecting with a degree and feeling of urgency. The different pads will be movable over screen, similar as to a whiteboard where you can move things around. Each of those pads has 4 different elements that are shown:
- ATC Event (you can chose different setups)
- Select a status (you can chose between Information, Caution and Alert. Color needs to feel more alert from Information to Alert.
- Notes box (you can open the box and write additional text on it)
- Music (you can chose different files. on the right side you can see a small group of notes. When you hover over the notes, music will be played without pressing a play or stop button.
The second video is an overview of music archival program that is connected with the pads.
Look and feel
Each slider illustrates characteristics of the customer's brand and the style your logo design should communicate.

```html
<!DOCTYPE html>
<html lang="en">
<head>
<meta charset="utf-8">
<title>New Pad – Music Selection</title>
<link rel="stylesheet" href="https://fonts.googleapis.com/css2?family=Inter:wght@400;500;600;700&display=swap">
<style>
:root{
  --backdrop:#4a4a62;
  --navy:#3c3f7d;
  --navy-deep:#33366c;
  --navy-light:#4a4e92;
  --orange:#fdab0b;
  --field:#f6f4fc;
  --field-border:#e7e4f2;
  --ink:#1d1d2b;
  --muted:#9a97b8;
  --white:#ffffff;
  --pad-green:#7cf59a;
  --pad-red:#f37b7b;
  --pad-yellow:#f6f59a;
  --pad-blue:#6e72b8;
}
*{box-sizing:border-box;margin:0;padding:0}
html,body{width:1200px;height:675px;overflow:hidden}
body{font-family:"Inter",sans-serif;background:var(--backdrop);position:relative}
.board{position:absolute;inset:0;overflow:hidden;filter:blur(18px)}
.board .pad{position:absolute;border-radius:14px}
.board .dim{position:absolute;inset:0;background:rgba(60,60,80,.45)}
.modal{position:absolute;left:414px;top:125px;width:372px;height:425px;background:var(--white);border-radius:12px;overflow:hidden;box-shadow:0 10px 40px rgba(0,0,0,.25)}
.modal-header{position:relative;height:97px;background:linear-gradient(100deg,var(--navy-deep),var(--navy) 50%,var(--navy-light));color:var(--white)}
.header-art{position:absolute;inset:0;background:linear-gradient(120deg,rgba(255,255,255,0) 20%,rgba(255,255,255,.05) 50%,rgba(255,255,255,0) 80%)}
.tower-art{position:absolute;left:12px;top:45px;width:37px;height:52px;background:rgba(255,255,255,.85);border-radius:4px 4px 0 0}
.pad-code{position:absolute;left:15px;top:14px;font-size:11px;font-weight:700;opacity:.85}
.close{position:absolute;right:15px;top:14px;width:14px;height:14px}
.title{position:absolute;left:65px;top:55px;font-size:15px;font-weight:700}
.subtitle{position:absolute;left:65px;top:75px;font-size:10px;font-weight:600;opacity:.9}
.section-label{position:absolute;top:122px;font-size:9px;font-weight:500;color:var(--ink)}
.field{position:absolute;left:19px;width:150px;background:var(--field);border:1px solid var(--field-border);border-radius:8px;font-size:9px;color:var(--ink);font-weight:500}
.select{height:35px;display:flex;align-items:center;justify-content:space-between;padding:0 10px 0 9px}
.note{top:233px;height:81px;padding:13px 9px}
.note span{color:var(--muted)}
.search{position:absolute;left:343px;top:123px;width:9px;height:9px}
.track{position:absolute;left:194px;width:159px;height:35px;border-radius:7px;background:var(--navy);color:var(--white);display:flex;align-items:center;padding:0 8px}
.track.selected{background:var(--orange)}
.play{width:20px;height:20px;border-radius:50%;background:var(--orange);display:flex;align-items:center;justify-content:center;flex:none}
.selected .play{background:rgba(255,255,255,.35)}
.track-info{margin-left:7px;flex:1;line-height:1.15;white-space:nowrap}
.track-name{font-size:8.5px;font-weight:500}
.track-time{font-size:7.5px;font-weight:600}
.selected .track-info{color:#6d4a1a}
.check{width:13px;height:13px;border:1.5px solid var(--orange);border-radius:3px;flex:none}
.selected .check{background:var(--white);border-color:var(--white);display:flex;align-items:center;justify-content:center}
.scrollbar{position:absolute;left:359px;top:141px;width:1.5px;height:157px;background:#e8e6f1}
.scrollbar::before{content:"";position:absolute;left:0;top:0;width:100%;height:60px;background:var(--navy)}
.modal-footer{position:absolute;left:0;right:0;top:366px;bottom:0;border-top:1px solid #eeedf3}
.link-create{position:absolute;left:117px;top:26px;font-size:8.5px;font-weight:600;color:var(--orange);text-decoration:underline}
.btn-create{position:absolute;left:201px;top:12px;width:150px;height:35px;border-radius:12px;background:var(--orange);color:var(--white);font-size:8.5px;font-weight:600;display:flex;align-items:center;justify-content:center}
</style>
</head>
<body>
<div class="board" aria-hidden="true">
  <div class="pad" style="left:22px;top:95px;width:165px;height:70px;background:var(--pad-blue)"></div>
  <div class="pad" style="left:22px;top:180px;width:165px;height:130px;background:var(--pad-green)"></div>
  <div class="pad" style="left:215px;top:150px;width:170px;height:80px;background:var(--pad-blue)"></div>
  <div class="pad" style="left:215px;top:235px;width:170px;height:130px;background:var(--pad-red)"></div>
  <div class="pad" style="left:215px;top:400px;width:170px;height:70px;background:var(--pad-blue)"></div>
  <div class="pad" style="left:215px;top:480px;width:170px;height:135px;background:var(--pad-red)"></div>
  <div class="pad" style="left:600px;top:110px;width:170px;height:60px;background:var(--pad-blue)"></div>
  <div class="pad" style="left:600px;top:520px;width:170px;height:70px;background:var(--pad-green)"></div>
  <div class="pad" style="left:800px;top:350px;width:170px;height:80px;background:var(--pad-blue)"></div>
  <div class="pad" style="left:800px;top:435px;width:170px;height:135px;background:var(--pad-yellow)"></div>
  <div class="pad" style="left:990px;top:140px;width:170px;height:80px;background:var(--pad-blue)"></div>
  <div class="pad" style="left:990px;top:225px;width:170px;height:120px;background:var(--pad-red)"></div>
  <div class="dim"></div>
</div>

<div class="modal">
  <div class="modal-header">
    <div class="header-art" role="img" aria-label="Night sky illustration with clouds and a small airplane"></div>
    <div class="tower-art" role="img" aria-label="Control tower illustration"></div>
    <div class="pad-code">SO1</div>
    <svg class="close" viewBox="0 0 14 14"><path d="M1 1L13 13M13 1L1 13" stroke="#fff" stroke-width="1.4"/></svg>
    <div class="title">New</div>
    <div class="subtitle">Direct and organize your aircraft with the world of music</div>
  </div>

  <div class="section-label" style="left:19px">Basic Info</div>
  <div class="field select" style="top:141px">Select ATC event
    <svg width="8" height="5" viewBox="0 0 8 5"><path d="M1 1l3 3 3-3" fill="none" stroke="#1d1d2b" stroke-width="1.3"/></svg></div>
  <div class="field select" style="top:187px">Select ATC event
    <svg width="8" height="5" viewBox="0 0 8 5"><path d="M1 1l3 3 3-3" fill="none" stroke="#1d1d2b" stroke-width="1.3"/></svg></div>
  <div class="field note">Note<span>(If any)</span></div>

  <div class="section-label" style="left:195px">Choose your music</div>
  <svg class="search" viewBox="0 0 10 10"><circle cx="4.3" cy="4.3" r="3.2" fill="none" stroke="#3c3f7d" stroke-width="1.2"/><path d="M6.7 6.7L9 9" stroke="#3c3f7d" stroke-width="1.2"/></svg>

  <div class="track" style="top:141px">
    <div class="play"><svg width="7" height="8" viewBox="0 0 7 8"><path d="M0 0L7 4L0 8Z" fill="#fff"/></svg></div>
    <div class="track-info"><div class="track-name">Delmaro - Silver Tide</div><div class="track-time">03:54</div></div>
    <div class="check"></div>
  </div>
  <div class="track selected" style="top:187px">
    <div class="play"><svg width="7" height="8" viewBox="0 0 7 8"><path d="M0 0L7 4L0 8Z" fill="#fff"/></svg></div>
    <div class="track-info"><div class="track-name">Delmaro - Silver Tide</div><div class="track-time">03:54</div></div>
    <div class="check"><svg width="8" height="6" viewBox="0 0 8 6"><path d="M1 3l2 2 4-4" fill="none" stroke="#fdab0b" stroke-width="1.4"/></svg></div>
  </div>
  <div class="track" style="top:233px">
    <div class="play"><svg width="7" height="8" viewBox="0 0 7 8"><path d="M0 0L7 4L0 8Z" fill="#fff"/></svg></div>
    <div class="track-info"><div class="track-name">Delmaro - Silver Tide</div><div class="track-time">03:54</div></div>
    <div class="check"></div>
  </div>
  <div class="track" style="top:279px">
    <div class="play"><svg width="7" height="8" viewBox="0 0 7 8"><path d="M0 0L7 4L0 8Z" fill="#fff"/></svg></div>
    <div class="track-info"><div class="track-name">Delmaro - Silver Tide</div><div class="track-time">03:54</div></div>
    <div class="check"></div>
  </div>
  <div class="scrollbar"></div>

  <div class="modal-footer">
    <span class="link-create">Create</span>
    <div class="btn-create">Create</div>
  </div>
</div>
</body>
</html>
```